Flyer for our prophetic church event

I need a flyer designed for the launching of our "Nine Radiant Lord's Day Gatherings" event. This event should high light the next 7 Sundays starting on February the 11th, 2018

Event Name:
Nine Radiant Lord's Days

Event Slogan or topic:
Go and tell John ... the blind see, the lame walk, the lepers are cleansed, the deaf hear, the dead are raised,
the poor have the gospel preached to them.

Speaker:
Prophet Tomas Okello

February 11th
February 18th
February 25th
March 4th
March 11th
March 18th
March 25th

Location:
Halvor Community Center
382 Wendle Street
Portland, ME 04102
United States

Time:
10:00AM - 12:00PM

We welcome you all in the name of Jesus Christ

Contact Info:
Tel:+1(207) 555 3184 - Email:contact@brightmeadowfold.org - Website: http://velkor.org

Target Market(s)

Young adults

Industry/Entity Type

Church

Font styles to use
Other font styles liked:
• Surprise me, I trust the designers skills

Colors

Designer to choose colors to be used in the design.

Requirements
Must have
• The Velkor logo
• Tomas Okello's picture
• The
Should not have
• The background of the Tomas Okello's picture

```html
<!DOCTYPE html>
<html lang="en">
<head>
<meta charset="utf-8">
<title>Nine Radiant Lord's Days — Velkor</title>
<link href="https://fonts.googleapis.com/css2?family=Montserrat:wght@500;600;700;800;900&family=Dancing+Script:wght@500;600&display=swap" rel="stylesheet">
<style>
  :root {
    --orange: #f39a2b;
    --navy: #123a63;
    --navy-deep: #0f3358;
    --ink: #111316;
    --white: #ffffff;
    --sky-1: #a9cfd1;
    --sky-2: #7fb2b8;
    --earth: #8c6a45;
  }
  * { margin: 0; padding: 0; box-sizing: border-box; }
  html, body { width: 927px; height: 1200px; overflow: hidden; }
  body { font-family: "Montserrat", sans-serif; }
  .flyer { position: relative; width: 927px; height: 1200px; overflow: hidden; }

  .backdrop {
    position: absolute; inset: 0;
    background:
      radial-gradient(ellipse 300px 420px at 330px 700px, rgba(140,106,69,.75), rgba(140,106,69,0) 70%),
      radial-gradient(ellipse 260px 320px at 800px 280px, rgba(150,150,140,.55), rgba(150,150,140,0) 70%),
      linear-gradient(170deg, var(--sky-1), var(--sky-2) 60%, #9bb9a9);
  }

  .title-band {
    position: absolute; left: 0; top: 44px; width: 668px; height: 174px;
    background: var(--orange); overflow: hidden;
  }
  .title-emblem {
    position: absolute; left: 96px; top: 56px; width: 180px; height: 152px;
    border-radius: 50%; background: rgba(255,255,255,.35);
  }
  .title-count {
    position: absolute; left: 96px; top: 104px; width: 180px; text-align: center;
    font-weight: 800; font-size: 50px; line-height: 1; color: var(--navy);
  }
  .title-text {
    position: absolute; left: 284px; top: 74px; width: 370px;
    font-weight: 800; color: var(--navy); line-height: 1; white-space: nowrap;
  }
  .title-text .line-1 { display: block; font-size: 52px; letter-spacing: 1px; }
  .title-text .line-2 { display: block; font-size: 47px; margin-top: 8px; }

  .brand-box {
    position: absolute; left: 677px; top: 44px; width: 250px; height: 174px;
    background: var(--navy-deep);
    display: flex; align-items: center; justify-content: center; gap: 12px;
  }
  .brand-dot { width: 18px; height: 18px; border-radius: 50%; background: var(--orange); }
  .brand-name { font-weight: 600; font-size: 40px; color: var(--white); letter-spacing: 2px; }

  .verse {
    position: absolute; left: 168px; top: 234px; width: 592px; text-align: center;
    font-family: "Dancing Script", cursive; font-weight: 500; font-size: 24px;
    line-height: 34px; color: #1d2a3a;
  }

  .dates {
    position: absolute; left: 497px; top: 362px; list-style: none;
    font-weight: 800; font-size: 30px; line-height: 45.5px; color: var(--ink);
  }

  .band { position: absolute; }
  .band-location { left: 0; top: 704px; width: 927px; height: 33px; background: rgba(18,58,99,.85); }
  .band-time { left: 5px; top: 901px; width: 922px; height: 36px; background: rgba(243,154,43,.9); }
  .band-label {
    position: absolute; left: 496px; font-weight: 600; font-size: 24px; line-height: 1;
    font-variant: small-caps; letter-spacing: 1.5px;
  }
  .band-location .band-label { top: 4px; color: var(--white); }
  .band-time .band-label { left: 491px; top: 6px; color: var(--white); }

  .portrait {
    position: absolute; left: 72px; top: 420px; width: 318px; height: 388px;
    border-radius: 50%; border: 4px solid var(--white);
    background: radial-gradient(ellipse at 50% 40%, #6a5b55, #2a2a30 65%, #b9a8a2);
  }

  .speaker {
    position: absolute; left: 70px; top: 833px; width: 362px; text-align: center;
  }
  .speaker-name {
    font-weight: 700; font-size: 25px; font-variant: small-caps; letter-spacing: 1px;
    color: var(--white);
  }
  .speaker-role { font-weight: 500; font-size: 22px; color: var(--ink); margin-top: 0; }

  .address {
    position: absolute; left: 496px; top: 746px; font-style: normal;
    font-weight: 500; font-size: 24px; line-height: 32px; color: var(--navy);
  }
  .time {
    position: absolute; left: 496px; top: 951px;
    font-weight: 500; font-size: 22px; color: var(--navy);
  }

  .welcome {
    position: absolute; left: 0; top: 1008px; width: 927px; text-align: center;
    font-family: "Dancing Script", cursive; font-weight: 600; font-size: 40px; color: var(--ink);
  }

  .contact { position: absolute; top: 1092px; height: 55px; display: flex; align-items: center; gap: 10px;
    font-weight: 600; font-size: 22px; }
  .contact-phone { left: 0; width: 460px; background: var(--navy-deep); color: var(--white); justify-content: center; font-size: 24px; }
  .contact-email { left: 468px; width: 459px; background: var(--orange); color: var(--navy); padding-left: 28px; }
  .contact svg { flex: none; }

  .website {
    position: absolute; left: 0; top: 1155px; width: 927px; text-align: center;
    font-weight: 700; font-size: 22px; letter-spacing: 2px; color: var(--white);
  }
</style>
</head>
<body>
<main class="flyer">
  <div class="backdrop" role="img" aria-label="Soft painting of Jesus raising a hand against a pale sky"></div>

  <header>
    <div class="title-band"></div>
    <div class="title-emblem" role="img" aria-label="White crown of thorns emblem"></div>
    <div class="title-count">NINE</div>
    <h1 class="title-text"><span class="line-1">RADIANT</span><span class="line-2">LORD'S DAY</span></h1>
    <div class="brand-box"><span class="brand-dot"></span><span class="brand-name">VELKOR</span></div>
  </header>

  <p class="verse">Go and tell John ... the blind see, the lame walk, the lepers are cleansed, the deaf hear, the dead are raised, the poor have the gospel preached to them.</p>

  <ul class="dates">
    <li>February 11th</li>
    <li>February 18th</li>
    <li>February 25th</li>
    <li>March 4th</li>
    <li>March 11th</li>
    <li>March 18th</li>
    <li>March 25th</li>
  </ul>

  <div class="band band-location"><span class="band-label">Location:</span></div>
  <div class="band band-time"><span class="band-label">Time:</span></div>

  <div class="portrait" role="img" aria-label="Portrait photo of the speaker, Prophet Tomas Okello"></div>
  <div class="speaker">
    <div class="speaker-name">Prophet Tomas Okello</div>
    <div class="speaker-role">Speaker</div>
  </div>

  <address class="address">Halvor Community Center<br>382 Wendle Street<br>Portland, ME 04102<br>United States</address>
  <div class="time">10:00AM - 12:00PM</div>

  <p class="welcome">We welcome you all in the name of Jesus Christ</p>

  <div class="contact contact-phone">
    <svg width="22" height="22" viewBox="0 0 24 24" fill="none" stroke="#fff" stroke-width="1.8"><circle cx="12" cy="12" r="10"/><path d="M9 7.5c-1 1-1 3 1.2 5.6 2.3 2.6 4.3 3 5.3 2.1l.8-.9-2-1.7-1 .8c-.8-.3-2.4-2-2.7-2.8l.8-1-1.7-2z"/></svg>
    <span>+1(207) 555 3184</span>
  </div>
  <div class="contact contact-email">
    <svg width="22" height="18" viewBox="0 0 24 18" fill="none" stroke="#123a63" stroke-width="1.8"><rect x="1" y="1" width="22" height="16"/><path d="M1 1l11 9 11-9"/></svg>
    <span>contact@brightmeadowfold.org</span>
  </div>

  <div class="website">www.velkor.org</div>
</main>
</body>
</html>
```